KPT Building And Maintenance

Need a very professional looking double sided Buisiness card with all my details phone number, name, email, license number.

Target Market(s)

construction industry

Industry/Entity Type

building

Contact Information for Business Card

Name Dale Whitcombe. Email Address Info@KPTBuilding.example.au mobile number 0452918730 licence number 871406D. web site

```html
<!DOCTYPE html>
<html lang="en">
<head>
<meta charset="utf-8">
<title>KPT Building And Maintenance – Business Card</title>
<link rel="stylesheet" href="https://fonts.googleapis.com/css2?family=Exo+2:wght@400;600;800&display=swap">
<style>
  :root {
    --stage: #2b2b2d;
    --navy: #070d1c;
    --sky: #08a0e6;
    --sky-light: #3d99e0;
    --white: #ffffff;
    --ink: #111111;
  }
  * { margin: 0; padding: 0; box-sizing: border-box; }
  html, body { width: 1200px; height: 1015px; overflow: hidden; }
  body {
    background: var(--stage);
    font-family: "Exo 2", sans-serif;
    position: relative;
  }
  .card {
    position: absolute;
    left: 250px;
    width: 700px;
    height: 400px;
    overflow: hidden;
    box-shadow: 0 10px 30px rgba(0,0,0,.5);
  }

  /* Back side */
  .card-back { top: 70px; background: var(--navy); }
  .back-brand {
    position: absolute;
    top: 170px; left: 0; width: 100%;
    display: flex; align-items: center; justify-content: center; gap: 12px;
  }
  .back-brand .brand-name { color: var(--white); }
  .back-web {
    position: absolute;
    top: 300px; left: 0; width: 100%;
    display: flex; align-items: center; justify-content: center; gap: 14px;
    font-size: 17px; letter-spacing: 2px;
    color: var(--white);
  }
  .back-web .hl { color: var(--sky-light); }
  .back-rule { width: 110px; height: 1px; background: var(--sky-light); }

  /* Shared brand lockup */
  .brand-dot { width: 14px; height: 14px; background: var(--sky); flex: none; }
  .brand-name {
    font-weight: 600; font-size: 28px; letter-spacing: 2px;
    color: var(--white); text-transform: uppercase; white-space: nowrap;
  }

  /* Front side */
  .card-front { top: 545px; background: var(--white); }
  .front-head {
    position: absolute; top: 0; left: 0; width: 100%; height: 150px;
    background: var(--navy);
    display: flex; align-items: center; justify-content: center; gap: 12px;
  }
  .front-band {
    position: absolute; top: 150px; left: 0; width: 700px; height: 115px;
    background: var(--sky);
  }
  .front-band-low {
    position: absolute; top: 265px; left: 0; width: 360px; height: 65px;
    background: var(--sky);
  }
  .holder {
    position: absolute; top: 218px; left: 30px; width: 330px;
    font-weight: 800; font-size: 32px; letter-spacing: 1.5px;
    color: var(--white); text-transform: uppercase; white-space: nowrap;
  }
  .divider {
    position: absolute; top: 168px; left: 380px;
    width: 1px; height: 80px; background: var(--white);
  }
  .contacts {
    position: absolute; top: 172px; left: 398px;
    list-style: none;
    font-size: 16px; letter-spacing: .5px; color: var(--white);
  }
  .contacts li { display: flex; align-items: center; gap: 10px; height: 24px; white-space: nowrap; }
  .contacts svg { width: 15px; height: 15px; flex: none; }
  .licence {
    position: absolute; top: 284px; left: 400px;
    font-size: 21px; letter-spacing: 1px; color: var(--sky); white-space: nowrap;
  }
  .licence .num { color: var(--ink); }
  .strip-dark {
    position: absolute; bottom: 0; left: 0; width: 350px; height: 12px;
    background: var(--navy);
  }
  .strip-blue {
    position: absolute; bottom: 0; left: 356px; width: 344px; height: 12px;
    background: var(--sky-light);
  }
</style>
</head>
<body>

<section class="card card-back">
  <div class="back-brand">
    <span class="brand-dot"></span>
    <span class="brand-name">KPT Building And Maintenance</span>
  </div>
  <div class="back-web">
    <span class="back-rule"></span>
    <span>www.<span class="hl">KPTBuilding</span>.example.au</span>
    <span class="back-rule"></span>
  </div>
</section>

<section class="card card-front">
  <header class="front-head">
    <span class="brand-dot"></span>
    <span class="brand-name">KPT Building And Maintenance</span>
  </header>
  <div class="front-band"></div>
  <div class="front-band-low"></div>
  <div class="holder">Dale Whitcombe</div>
  <div class="divider"></div>
  <ul class="contacts">
    <li>
      <svg viewBox="0 0 24 24" fill="#fff"><path d="M6.6 10.8a15.1 15.1 0 0 0 6.6 6.6l2.2-2.2a1 1 0 0 1 1-.25 11.4 11.4 0 0 0 3.6.57 1 1 0 0 1 1 1V20a1 1 0 0 1-1 1A17 17 0 0 1 3 4a1 1 0 0 1 1-1h3.5a1 1 0 0 1 1 1c0 1.25.2 2.45.57 3.57a1 1 0 0 1-.25 1z"/></svg>
      0452918730
    </li>
    <li>
      <svg viewBox="0 0 24 24" fill="none" stroke="#fff" stroke-width="2"><rect x="2" y="5" width="20" height="14"/><path d="M2 5l10 8 10-8"/></svg>
      Info@KPTBuilding.example.au
    </li>
    <li>
      <svg viewBox="0 0 24 24" fill="none" stroke="#fff" stroke-width="1.8"><circle cx="12" cy="12" r="10"/><path d="M2 12h20M12 2c3 3 3 17 0 20M12 2c-3 3-3 17 0 20"/></svg>
      www.KPTBuilding.example.au
    </li>
  </ul>
  <div class="licence">Licence No. <span class="num">871406D</span></div>
  <div class="strip-dark"></div>
  <div class="strip-blue"></div>
</section>

</body>
</html>
```